Medical Centre Website

We need a new design for a medical centre based in Perth, Western Australia called 'Tarvin Grove Medical Centre'.

The medical centre does general practitioner work including general checkups, ecg, heart checks, woman's health and more servicing children and adults. They also do home visits on occasions where the patient cannot attend the centre.

They would like an information/brochure website where visitors can read up on the practice, send email and view their location.

The client wish the design to be clean, fresh and light. The main colours are a light purple/blue and to a dark navy blue. The client would not want the logo to be altered in any way. This includes changing the words colours or the image.

The final design should represent a loving, family friendly practice where patients can come to receive the best treatments.

We just need the end product to be presented to un in a layed psd format. The fonts must be as per the W3C standards.

**IMPORTANT**
I have received heaps of chatlink invites in the past. To treat everyone fairly, I do not add people to my chatlink list as in the past people expected us to give them the prize. If you have questions, please ask them in pixel forum as it may benefit others who are also designing the site. If I need to, I will send a message to the user.
Updates

Hi Designers,

Most designs we have received have been overly cluttered. Are you able to simplify the designs.

Cheers, Dorian

Hi Designers,

Some of the designs are quite attractive but aremore cluttered than I would like. If you have a look at the following design, the design is very simple and straight to the point. A lot of designs have too much wording and the reader can be put off. We are looking something more like:

velmoxa.com.au

I would prefer to see designs and have opened up the contest for a further 7 days.

Designers,

We have received feedback from the client and Quite frankly he don’t really like any of them.They are too cluttered and Americanised. All drab blue colours.
 
If you have a look at template monster, these designs are better and cleaner. We do not want heaps of writing on the front page.

If you look at the eariler examples such as quorbeyclinic.com.au which I did myself, the client loves that simplicity of the site.

```html
<!DOCTYPE html>
<html lang="en">
<head>
<meta charset="utf-8">
<title>Tarvin Grove Medical Centre</title>
<link rel="stylesheet" href="https://fonts.googleapis.com/css2?family=Open+Sans:wght@400;600;700&family=Tinos:wght@400;700&display=swap">
<style>
  :root {
    --page-bg: #1d4f8e;
    --navy: #0d4f9a;
    --navy-dark: #0a3f7c;
    --heading-blue: #1b5ba8;
    --lavender: #93a6d6;
    --lavender-light: #a9b8e0;
    --text: #444;
    --muted: #777;
    --rule: #dcdcdc;
    --panel-grey: #efefef;
    --footer-link: #a9bfe0;
    --white: #fff;
  }
  * { box-sizing: border-box; margin: 0; padding: 0; }
  html, body { width: 1093px; height: 1200px; overflow: hidden; }
  body {
    background: var(--page-bg);
    font-family: "Open Sans", Arial, sans-serif;
    color: var(--text);
  }
  .site { position: relative; width: 911px; margin: 18px 0 0 91px; }

  /* Header */
  .masthead {
    height: 100px; background: var(--white);
    display: flex; align-items: center; justify-content: space-between;
    padding: 0 12px 0 16px;
  }
  .brand { display: flex; align-items: center; gap: 10px; }
  .brand-mark { width: 14px; height: 14px; background: var(--lavender); border-radius: 50%; }
  .brand-name {
    font-family: "Tinos", "Times New Roman", serif; font-size: 30px; font-weight: 400;
    color: var(--heading-blue); letter-spacing: .5px;
  }
  .email-btn {
    display: flex; align-items: center; gap: 8px;
    height: 35px; padding: 0 14px;
    background: var(--lavender); border: 2px solid #b8c5e8; border-radius: 5px;
    color: var(--white); font-family: "Tinos", serif; font-weight: 700; font-size: 15px;
    text-decoration: none;
  }

  /* Navigation */
  .main-nav { background: var(--white); border-top: 1px solid #eee; border-bottom: 3px solid var(--navy); }
  .main-nav ul { list-style: none; display: flex; height: 37px; align-items: center; }
  .main-nav li { flex: 1; text-align: center; font-size: 13px; color: var(--heading-blue); border-left: 1px solid #e6e6e6; line-height: 27px; }
  .main-nav li:first-child { border-left: 0; color: #111; }

  /* Hero */
  .hero { display: flex; height: 333px; border-bottom: 3px solid var(--navy); }
  .hero-panel { width: 371px; background: var(--lavender); padding: 44px 18px 0 19px; position: relative; }
  .hero-title {
    font-family: "Tinos", serif; font-weight: 400; font-size: 34px; line-height: 40px;
    color: var(--white); text-transform: uppercase; letter-spacing: -.5px;
    padding-bottom: 18px; border-bottom: 1px solid var(--lavender-light);
  }
  .hero-text { color: var(--white); font-size: 12px; line-height: 19px; margin-top: 16px; }
  .btn {
    display: inline-block; background: var(--navy); color: var(--white);
    border: 1px solid #5a8bd0; font-size: 12.5px; padding: 4px 13px; text-decoration: none;
  }
  .hero .btn { margin-top: 22px; padding: 7px 10px; }
  .slider-dots { position: absolute; left: 21px; bottom: 16px; display: flex; gap: 4px; }
  .slider-dots span { width: 8px; height: 8px; border-radius: 50%; background: #c4cfea; }
  .slider-dots span:first-child { background: var(--white); }
  .hero-photo { flex: 1; background: linear-gradient(120deg, #3b3530 0%, #e8e4df 35%, #f4f1ee 60%, #b9c9bd 85%, #8fb9a2 100%); }

  /* Content */
  .content { background: var(--white); height: 326px; display: flex; padding: 30px 0 30px; }
  .col { padding: 0 17px; display: flex; flex-direction: column; }
  .col .btn { margin-top: auto; align-self: flex-start; }
  .col + .col { border-left: 1px solid #e2e2e2; }
  .col-about { width: 413px; }
  .col-news { width: 249px; }
  .col-contact { flex: 1; padding-right: 18px; }
  .section-title { font-family: "Tinos", serif; font-weight: 400; font-size: 19px; line-height: 22px; color: var(--heading-blue); margin-bottom: 10px; }
  .col-about .section-title { margin-bottom: 8px; }
  .about-photo { width: 377px; height: 82px; flex: none; background: linear-gradient(100deg, #5f8ad0 0%, #c6413a 40%, #2f5ea8 55%, #d9d9d9 80%, #b6b6b6 100%); border: 1px solid #ccc; }
  .about-text { font-size: 11.2px; line-height: 17.8px; letter-spacing: -.1px; margin: 12px 0 4px; }
  .news-item { font-size: 10px; line-height: 13.3px; color: #333; margin-bottom: 15px; }
  .news-item::after { content: ""; display: block; clear: both; }
  .news-thumb { float: left; width: 52px; height: 52px; margin: 0 11px 2px 0; }
  .news-item h4 { font-size: 11.5px; font-weight: 700; margin-bottom: 2px; }
  .contact-intro { font-size: 12px; line-height: 14.5px; padding-bottom: 10px; border-bottom: 1px solid var(--rule); margin-bottom: 10px; }
  .field-label { display: block; font-size: 11px; line-height: 13px; margin-bottom: 3px; }
  .field {
    display: block; width: 214px; height: 22px; margin-bottom: 6px; flex: none;
    border: 1px solid #e0e0e0; border-radius: 3px; background: #fafafa;
    font-family: inherit; font-size: 8.5px; font-style: italic; color: #aaa; padding: 0 8px;
  }
  textarea.field { height: 42px; padding-top: 6px; resize: none; }

  /* Services */
  .services { background: var(--panel-grey); height: 130px; padding: 18px 20px 0 17px; border-top: 1px solid #ddd; }
  .services-head { display: flex; align-items: center; gap: 10px; }
  .services-head h2 { font-family: "Tinos", serif; font-weight: 700; font-size: 20px; color: var(--heading-blue); white-space: nowrap; }
  .services-head::after { content: ""; flex: 1; height: 1px; background: var(--rule); }
  .service-list { list-style: none; display: flex; margin-top: 16px; }
  .service { display: flex; align-items: center; gap: 10px; font-family: "Tinos", serif; font-size: 17.5px; color: #222; }
  .service:nth-child(1) { width: 221px; }
  .service:nth-child(2) { width: 254px; }
  .service:nth-child(3) { width: 219px; }
  .service-icon { width: 48px; height: 48px; }

  /* Footer */
  .site-footer { height: 252px; position: relative; color: var(--white); }
  .footer-cols { display: flex; padding-top: 27px; }
  .footer-col h3 { font-size: 14px; font-weight: 700; margin-bottom: 10px; }
  .footer-col ul { list-style: none; }
  .footer-col li { font-size: 11px; line-height: 21px; color: var(--footer-link); }
  .footer-col:nth-child(1) { width: 187px; }
  .footer-col:nth-child(2) { width: 179px; }
  .footer-col:nth-child(3) { width: 178px; }
  .footer-col:nth-child(4) { width: 158px; }
  .social { display: flex; gap: 14px; margin-top: 4px; }
  .social span { width: 22px; height: 22px; border-radius: 50%; background: #3f6faa; }
  .footer-brand { position: absolute; left: 702px; top: 130px; display: flex; align-items: center; gap: 7px; }
  .footer-brand .brand-mark { background: #8fa8d4; width: 11px; height: 11px; }
  .footer-brand .brand-name { color: #c8d4ea; font-size: 20px; }
  .copyright { position: absolute; left: 0; right: 0; top: 206px; border-top: 1px solid #2f63a4; padding-top: 16px; font-size: 11px; color: #c0cfe6; }
</style>
</head>
<body>
<div class="site">
  <header class="masthead">
    <div class="brand"><span class="brand-name">Tarvin Grove Medical Centre</span><span class="brand-mark"></span></div>
    <a class="email-btn" href="#">
      <svg width="15" height="11" viewBox="0 0 15 11" aria-hidden="true"><rect x=".5" y=".5" width="14" height="10" fill="none" stroke="#fff"/><path d="M.5 .5 7.5 6 14.5 .5" fill="none" stroke="#fff"/></svg>
      SEND US AN EMAIL
    </a>
  </header>

  <nav class="main-nav">
    <ul>
      <li>Home</li><li>About Us</li><li>Medical Services</li><li>Appointments</li><li>Our Doctors</li><li>Location</li>
    </ul>
  </nav>

  <section class="hero">
    <div class="hero-panel">
      <h1 class="hero-title">Our family caring<br>for your family</h1>
      <p class="hero-text">Le Lorem Ipsum est simplement du faux texte employé dans la composition et la mise en page avant impression. Le Lorem Ipsum est le faux texte standard de l'imprimerie depuis les années 1500.</p>
      <a class="btn" href="#">Read More</a>
      <div class="slider-dots"><span></span><span></span><span></span><span></span></div>
    </div>
    <div class="hero-photo" role="img" aria-label="Photo of a smiling nurse caring for an elderly patient"></div>
  </section>

  <section class="content">
    <div class="col col-about">
      <h2 class="section-title">About Tarvin Grove Medical Centre</h2>
      <div class="about-photo" role="img" aria-label="Photo of hospital signs for Emergency and Main Entrance"></div>
      <p class="about-text">On sait depuis longtemps que travailler avec du texte lisible et contenant du sens est source de distractions, et empêche de se concentrer sur la mise en page elle-même. L'avantage du Lorem Ipsum sur un texte générique comme 'Du texte. Du texte.Du texte.' est qu'il possède une distribution de lettres plus ou moins normale, et en tout cas comparable avec celle du français standard.</p>
      <a class="btn" href="#">Submit</a>
    </div>
    <div class="col col-news">
      <h2 class="section-title">Latest News</h2>
      <article class="news-item">
        <div class="news-thumb" role="img" aria-label="Photo of an elderly hand held in care" style="background:linear-gradient(135deg,#8a6d58,#d9b9a0,#c79a7c)"></div>
        <h4>On sait depuis longtemps</h4>
        avec du texte lisible et contenant du sens est source de distractions, et empêche de se avec du texte lisible et contenant du sens est source de distractions, et empêche de se concentrer sur la mise en.
      </article>
      <article class="news-item">
        <div class="news-thumb" role="img" aria-label="Photo of a hospital bed in a bright ward" style="background:linear-gradient(135deg,#9aa6b3,#e8ecef,#b8c2cc)"></div>
        <h4>Encore qu'à leur phase de</h4>
        avec du texte lisible et contenant du sens est source de distractions, et empêche de se avec du texte lisible et contenant du sens est source de distractions, et empêche de se concentrer sur la mise en.
      </article>
      <a class="btn" href="#">Submit</a>
    </div>
    <div class="col col-contact">
      <h2 class="section-title">Contact Us</h2>
      <p class="contact-intro">Please fill this form fot further information.</p>
      <label class="field-label">Name:</label>
      <input class="field" placeholder="Please enter your name..">
      <label class="field-label">Email:</label>
      <input class="field" placeholder="Please enter your name..">
      <label class="field-label">Comments:</label>
      <textarea class="field" placeholder="Please enter your comments.."></textarea>
      <a class="btn" href="#">Submit</a>
    </div>
  </section>

  <section class="services">
    <div class="services-head"><h2>OUR SERVICES</h2></div>
    <ul class="service-list">
      <li class="service">
        <svg class="service-icon" viewBox="0 0 48 48" aria-hidden="true"><circle cx="24" cy="24" r="23" fill="#0d4f9a" stroke="#5a8bd0" stroke-width="2"/><rect x="16" y="13" width="16" height="22" rx="2" fill="none" stroke="#fff" stroke-width="2"/><rect x="20" y="11" width="8" height="4" fill="#fff"/><path d="M19 21h10M19 25h10M19 29h10" stroke="#fff" stroke-width="1.5"/></svg>
        General checkups
      </li>
      <li class="service">
        <svg class="service-icon" viewBox="0 0 48 48" aria-hidden="true"><circle cx="24" cy="24" r="23" fill="#0d4f9a" stroke="#5a8bd0" stroke-width="2"/><rect x="11" y="15" width="26" height="18" rx="2" fill="none" stroke="#fff" stroke-width="2"/><path d="M13 25h5l2-5 3 9 3-7 2 3h8" fill="none" stroke="#fff" stroke-width="1.5"/></svg>
        Electrocardiography
      </li>
      <li class="service">
        <svg class="service-icon" viewBox="0 0 48 48" aria-hidden="true"><circle cx="24" cy="24" r="23" fill="#0d4f9a" stroke="#5a8bd0" stroke-width="2"/><circle cx="24" cy="24" r="13" fill="#fff"/><path d="M17 24l5 5 9-10" fill="none" stroke="#0d4f9a" stroke-width="3.5" stroke-linecap="round" stroke-linejoin="round"/></svg>
        Heart Checks
      </li>
      <li class="service">
        <svg class="service-icon" viewBox="0 0 48 48" aria-hidden="true"><circle cx="24" cy="24" r="23" fill="#0d4f9a" stroke="#5a8bd0" stroke-width="2"/><circle cx="24" cy="13" r="3" fill="#fff"/><path d="M24 17l-6 12h4v9h4v-9h4z" fill="#fff"/></svg>
        Woman's Health
      </li>
    </ul>
  </section>

  <footer class="site-footer">
    <div class="footer-cols">
      <div class="footer-col"><h3>Adipisicing elit</h3><ul><li>L'extrait standard</li><li>Utilisé depuis</li><li>XVIè siècle est</li><li>Reproduit</li><li>Dessous pour</li><li>Curieux les sections</li></ul></div>
      <div class="footer-col"><h3>Pendant la</h3><ul><li>L'extrait standard</li><li>Utilisé depuis</li><li>XVIè siècle est</li><li>Reproduit</li></ul></div>
      <div class="footer-col"><h3>Pour Générer</h3><ul><li>L'extrait standard</li><li>Utilisé depuis</li><li>XVIè siècle est</li><li>Reproduit</li><li>Dessous pour</li></ul></div>
      <div class="footer-col"><h3>Structures</h3><ul><li>L'extrait standard</li><li>Utilisé depuis</li><li>XVIè siècle est</li><li>Reproduit</li><li>Dessous pour</li><li>Curieux les sections</li></ul></div>
      <div class="footer-col"><h3>Follow Us</h3><div class="social"><span></span><span></span><span></span><span></span></div></div>
    </div>
    <div class="footer-brand"><span class="brand-name">Tarvin Grove</span><span class="brand-mark"></span></div>
    <p class="copyright">© Copyrights 2013 All rights Reserved</p>
  </footer>
</div>
</body>
</html>
```